New Zealand Export company needs business cards

We need new business cards to match our new logo for a company based in New Zealand who deal specifically with the Pacific Islands. We source, consolidate and ship products out of New Zealand to the Pacific Islands. Will attach our old ones and also new logo.
Would like the Islands we deal with and the areas of work we have access to, to be included on the business cards.

Contact Information for Business Card

T +64 9 381 5047
F +64 9 381 6620
12-18 Marlow Lane, Drury, 2113
PO Box 862, Drury, Auckland 2247, New Zealand
www.kestaltrade.co.nz
E sales@kestaltrade.co.nz

Font styles to use
Sans Serif

Colors
85abd2
33a6d7
ffffff

Requirements
Must have
• A company of WMB

```html
<!DOCTYPE html>
<html lang="en">
<head>
<meta charset="utf-8">
<title>Kestal Trade – Business Card</title>
<link href="https://fonts.googleapis.com/css2?family=Jost:wght@400;500;600&family=Oswald:wght@500&display=swap" rel="stylesheet">
<style>
  :root {
    --stage: #000000;
    --label: #8a8a8a;
    --card-white: #ffffff;
    --brand-blue: #33a6d7;
    --brand-navy: #1158a7;
    --soft-blue: #85abd2;
    --heading-tint: #c6e3f3;
    --list-tint: #e4f2fa;
    --icon-tint: #b9c9dc;
  }
  html, body {
    margin: 0; padding: 0;
    width: 1200px; height: 404px;
    overflow: hidden;
    background: var(--stage);
    font-family: "Jost", sans-serif;
  }
  .side-label {
    position: absolute; top: 12px;
    font-size: 15px; color: var(--label); letter-spacing: 0.5px;
  }
  .card {
    position: absolute; top: 37px;
    width: 552px; height: 337px;
    background: var(--card-white);
    overflow: hidden;
  }
  .card--front { left: 25px; }
  .card--back { left: 620px; }
  .card__band { position: absolute; inset: 0; }
  .wordmark {
    position: absolute;
    display: flex; align-items: center;
    color: var(--brand-navy);
    font-weight: 600; letter-spacing: 2px; white-space: nowrap;
  }
  .wordmark__square { background: var(--brand-navy); margin-right: 10px; }
  .wordmark--front { left: 76px; top: 46px; font-size: 34px; }
  .wordmark--front .wordmark__square { width: 30px; height: 30px; }
  .wordmark--back { left: 346px; top: 30px; font-size: 20px; letter-spacing: 1px; }
  .wordmark--back .wordmark__square { width: 18px; height: 18px; margin-right: 7px; }

  .contact-list { position: absolute; left: 43px; top: 232px; margin: 0; padding: 0; list-style: none; }
  .contact-list li {
    display: flex; align-items: center; height: 20.5px;
    color: var(--card-white); font-size: 15.5px;
  }
  .contact-list svg { width: 13px; height: 13px; margin-right: 12px; flex: none; }
  .address {
    position: absolute; left: 282px; top: 279px;
    color: var(--card-white); font-size: 11.5px; line-height: 17.5px;
  }
  .tagline {
    position: absolute; left: 194px; top: 92px; width: 336px;
    font-family: "Oswald", sans-serif; font-weight: 500;
    font-size: 20.5px; color: var(--card-white);
    letter-spacing: -0.2px; white-space: nowrap;
    transform: scaleX(0.9); transform-origin: left;
  }
  .section-title {
    position: absolute; top: 167px;
    font-family: "Oswald", sans-serif; font-weight: 500;
    font-size: 20px; color: var(--heading-tint);
    transform: scaleX(0.88); transform-origin: left;
  }
  .bullet-list { position: absolute; margin: 0; padding: 0; list-style: none; }
  .bullet-list li {
    position: relative; padding-left: 10px;
    color: var(--list-tint); font-size: 13.5px; line-height: 18px;
  }
  .bullet-list li::before {
    content: ""; position: absolute; left: 0; top: 8px;
    width: 5px; height: 2.5px; background: var(--list-tint);
  }
  .bullet-list--islands li { margin-bottom: 0; }
  .bullet-list--industries li { margin-bottom: 4.6px; }
  .bullet-list--industries-2 li { margin-bottom: 4.6px; line-height: 14px; padding-top: 2px; }
  .bullet-list--industries-2 li:first-child { margin-bottom: 7px; }
</style>
</head>
<body>
  <div class="side-label" style="left:25px">Front</div>
  <div class="side-label" style="left:620px">Back</div>

  <section class="card card--front">
    <svg class="card__band" viewBox="0 0 552 337" aria-hidden="true">
      <polygon fill="var(--brand-blue)" points="0,124 103,124 164,203 199,203 162,154 552,154 552,337 0,337"/>
    </svg>
    <div class="wordmark wordmark--front"><span class="wordmark__square"></span>KESTAL TRADE</div>

    <ul class="contact-list">
      <li><svg viewBox="0 0 12 12"><circle cx="6" cy="6" r="6" fill="var(--icon-tint)"/><path d="M3.6 3.2c.4-.4.9-.3 1.1.1l.5 1c.1.3 0 .6-.2.8l-.3.3c.4.8 1 1.4 1.8 1.8l.3-.3c.2-.2.5-.3.8-.2l1 .5c.4.2.5.7.1 1.1-.6.6-1.5.7-2.3.2C5.1 7.8 4.2 6.9 3.5 5.6c-.5-.8-.4-1.8.1-2.4z" fill="#fff"/></svg>+64 9 381 5047</li>
      <li><svg viewBox="0 0 12 12"><circle cx="6" cy="6" r="6" fill="var(--icon-tint)"/><rect x="4" y="3" width="4" height="2" fill="#fff"/><rect x="3" y="5" width="6" height="3" rx=".6" fill="#fff"/><rect x="4" y="7.5" width="4" height="1.8" fill="#fff"/></svg>+64 9 381 6620</li>
      <li><svg viewBox="0 0 12 12"><circle cx="6" cy="6" r="6" fill="var(--icon-tint)"/><circle cx="6" cy="6" r="3.2" fill="none" stroke="#fff" stroke-width=".9"/><path d="M2.8 6h6.4M6 2.8c-1.4 1.8-1.4 4.6 0 6.4M6 2.8c1.4 1.8 1.4 4.6 0 6.4" fill="none" stroke="#fff" stroke-width=".7"/></svg>www.kestaltrade.co.nz</li>
      <li><svg viewBox="0 0 12 12"><circle cx="6" cy="6" r="6" fill="var(--icon-tint)"/><rect x="3" y="3.8" width="6" height="4.4" fill="none" stroke="#fff" stroke-width=".9"/><path d="M3 3.8l3 2.4 3-2.4" fill="none" stroke="#fff" stroke-width=".9"/></svg>sales@kestaltrade.co.nz</li>
    </ul>

    <address class="address" style="font-style:normal">
      12-18 Marlow Lane, Drury, 2113<br>
      PO Box 862, Drury, Auckland 2247, New Zealand
    </address>
  </section>

  <section class="card card--back">
    <svg class="card__band" viewBox="0 0 552 337" aria-hidden="true">
      <polygon fill="var(--brand-blue)" points="0,58 103,58 164,137 199,137 161,87 552,87 552,337 0,337"/>
    </svg>
    <div class="wordmark wordmark--back"><span class="wordmark__square"></span>KESTAL TRADE</div>
    <div class="tagline">SUPPLYING THE PACIFIC FOR OVER 38 YEARS</div>

    <h2 class="section-title" style="left:41px;margin:0">ISLANDS</h2>
    <h2 class="section-title" style="left:330px;margin:0">INDUSTRIES</h2>

    <ul class="bullet-list bullet-list--islands" style="left:41px;top:194px">
      <li>Cook Island</li><li>Papua New Guinea</li><li>Tahiti</li>
      <li>Tuvalu</li><li>Fiji</li><li>Kiribati</li>
    </ul>
    <ul class="bullet-list bullet-list--islands" style="left:179px;top:194px">
      <li>Samoa</li><li>New Caledonia</li><li>Tonga</li>
      <li>Norfolk Island</li><li>Solomon Island</li><li>Vanutu</li>
    </ul>
    <ul class="bullet-list bullet-list--industries" style="left:330px;top:194px">
      <li>Hardware</li><li>Automotive</li><li>Homeware</li>
      <li>Aid Solution</li><li>Hospitality</li>
    </ul>
    <ul class="bullet-list bullet-list--industries-2" style="left:424px;top:194px">
      <li>Safe Equipment</li><li>Environmental<br>Resources</li>
    </ul>
  </section>
</body>
</html>
```